Flyer design

We need a marketing flyer to use when meeting with clients. We may also use it for mailings. Please see the attached document and images. Not all images need to be used. Please feel free to edit / photoshop images. Please also see our website : www.kelvorantissue.com

Industry/Entity Type

Marketing

```html
<!DOCTYPE html>
<html lang="en">
<head>
<meta charset="UTF-8">
<title>Kelvoran Tissue Diagnostics – Flyer</title>
<link href="https://fonts.googleapis.com/css2?family=PT+Sans:wght@400;700&family=PT+Sans+Narrow:wght@700&display=swap" rel="stylesheet">
<style>
  :root {
    --stage: #1b1b1b;
    --pink: #ee3f7c;
    --red: #e8261c;
    --red-deep: #c81a14;
    --ink: #1e1e1e;
    --white: #ffffff;
    --panel-dark: #1a1a1a;
    --tissue-a: #f06aa6;
    --tissue-b: #d9407f;
    --tissue-c: #b8306a;
  }
  * { margin: 0; padding: 0; box-sizing: border-box; }
  html, body { width: 1200px; height: 1000px; overflow: hidden; background: var(--stage); }
  body { position: relative; font-family: "PT Sans", Arial, sans-serif; }

  .flyer { position: absolute; left: 189px; top: 80px; width: 696px; height: 828px; background: var(--white); overflow: hidden; }
  .abs { position: absolute; }

  .top-bar { left: 0; top: 0; width: 696px; height: 15px; background: var(--pink); }
  .top-rule { left: 0; top: 15px; width: 325px; height: 8px; background: var(--red); }

  .brand { left: 0; top: 23px; width: 325px; height: 215px; background: var(--white); text-align: center; }
  .brand-name { position: absolute; left: 0; right: 0; top: 70px; display: flex; justify-content: center; align-items: center; gap: 12px; font-weight: 700; font-size: 44px; color: var(--ink); letter-spacing: 1px; }
  .brand-dot { width: 22px; height: 22px; border-radius: 50%; background: var(--red); }
  .brand-tag { position: absolute; left: 0; right: 0; top: 158px; font-size: 15px; letter-spacing: 9px; color: var(--red); }
  .brand-line { position: absolute; left: 0; right: 0; top: 178px; font-size: 14px; color: var(--ink); }

  .portrait { left: 325px; top: 23px; width: 371px; height: 215px; background: radial-gradient(ellipse at 55% 55%, #d9cfa8 0%, #8e8a76 45%, #2a2a2a 100%); }

  .tissue { left: 0; top: 238px; width: 696px; height: 337px; background: linear-gradient(120deg, var(--tissue-a) 0%, var(--tissue-b) 55%, var(--tissue-c) 100%); }

  .headline-band { left: 20px; top: 268px; width: 250px; height: 26px; background: linear-gradient(90deg, rgba(90,20,50,0.55), rgba(90,20,50,0)); }
  .headline-small { left: 24px; top: 264px; font-size: 28px; color: var(--white); }
  .headline-big { left: 22px; top: 289px; font-size: 56px; color: var(--ink); letter-spacing: -0.5px; line-height: 1; }

  .service-title { left: 28px; top: 378px; font-size: 28px; line-height: 38px; color: var(--ink); }
  .service-sub { left: 28px; top: 451px; font-size: 21px; line-height: 25px; color: var(--ink); }

  .name-band { left: 401px; top: 240px; width: 295px; height: 46px; background: linear-gradient(90deg, rgba(232,38,28,0.6), var(--red) 40%); }
  .doctor-name { left: 415px; top: 244px; font-family: "PT Sans Narrow", "Arial Narrow", sans-serif; font-weight: 700; font-size: 34px; color: var(--ink); white-space: nowrap; }
  .doctor-name small { font-size: 13px; }
  .credentials { right: 74px; top: 290px; text-align: right; color: var(--white); font-size: 15px; line-height: 22px; }
  .practice { right: 74px; top: 336px; text-align: right; color: var(--white); font-size: 19px; line-height: 24px; }

  .lab-photo { left: 418px; top: 418px; width: 278px; height: 150px; background: linear-gradient(135deg, #3a3f3c 0%, #8d948f 40%, #2b2e2d 75%, #c9a9d6 100%); border: 2px solid #222; }

  .services-band { left: 0; top: 575px; width: 696px; height: 110px; background: var(--red); }
  .service-list { left: 30px; top: 585px; list-style: none; color: var(--white); font-size: 15px; line-height: 20px; }
  .service-list li { position: relative; padding-left: 19px; }
  .service-list li::before { content: ""; position: absolute; left: 0; top: 5px; width: 9px; height: 9px; border-radius: 50%; background: var(--white); }
  .stains-note { right: 74px; top: 589px; width: 230px; text-align: right; color: var(--white); font-size: 13px; line-height: 17.5px; }

  .lens { left: 213px; top: 471px; width: 170px; height: 170px; border-radius: 50%; background: radial-gradient(circle at 45% 40%, #f0d7c0 0%, #c98f8f 45%, #6d3b4a 100%); box-shadow: 0 0 0 3px #3a2a2a, 0 6px 14px rgba(0,0,0,0.55); }

  .specimen { left: 0; top: 685px; width: 413px; height: 75px; background: linear-gradient(180deg, #d8c48c 0%, #c98a9a 55%, #d7c08b 100%); }
  .specimen-frame { left: 12px; top: 692px; width: 372px; height: 62px; border: 1px solid rgba(255,255,255,0.8); }

  .call-box { left: 0; top: 760px; width: 413px; height: 58px; background: var(--red); color: var(--white); padding: 10px 0 0 23px; }
  .call-line { font-size: 18px; }
  .address { display: flex; align-items: center; gap: 8px; font-size: 12px; margin-top: 4px; }
  .bottom-rule { left: 0; top: 818px; width: 350px; height: 10px; background: var(--red); }

  .logistics { left: 413px; top: 685px; width: 283px; height: 143px; background: var(--panel-dark); color: var(--white); font-size: 13px; line-height: 17.5px; text-align: right; padding: 15px 78px 0 20px; }
  .logistics p + p { margin-top: 19px; }
</style>
</head>
<body>
  <main class="flyer">
    <div class="abs top-bar"></div>
    <div class="abs top-rule"></div>

    <header class="abs brand">
      <div class="brand-name"><span class="brand-dot"></span><span>KELVORAN</span></div>
      <div class="brand-tag">TISSUE</div>
      <div class="brand-line">DIAGNOSTICS &amp; DERMATOPATHOLOGY</div>
    </header>

    <div class="abs portrait" role="img" aria-label="Portrait photograph of the physician in a dark suit and tie"></div>

    <div class="abs tissue" role="img" aria-label="Magnified pink skin tissue micrograph background"></div>

    <div class="abs headline-band"></div>
    <div class="abs headline-small">THE DIAGNOSIS</div>
    <h1 class="abs headline-big" style="font-weight:400">IN FOCUS.</h1>

    <h2 class="abs service-title" style="font-weight:400">Dermatopathology<br>consultative service</h2>
    <p class="abs service-sub">First or second opinions,<br>off-site or on-site.</p>

    <div class="abs name-band"></div>
    <div class="abs doctor-name">Lena M. Ortiz, <small>M.D.</small></div>
    <p class="abs credentials">Board Certified – Dermatopathology<br>Board Certified – Dermatology</p>
    <p class="abs practice">Practicing<br>Dermatopathology<br>since 2007.</p>

    <div class="abs lab-photo" role="img" aria-label="Microscope objective lens over an illuminated glass slide"></div>

    <div class="abs services-band"></div>
    <ul class="abs service-list">
      <li>Tissue processing</li>
      <li>Mohs technicians</li>
      <li>Immunohistochemistry<br>and special stains</li>
    </ul>
    <p class="abs stains-note">Access to an extensive range of special and immunohistochemistry stains, and patient-centered consideration of the judicious use of them.</p>

    <div class="abs lens" role="img" aria-label="Circular magnified view of stained tissue cells"></div>

    <div class="abs specimen" role="img" aria-label="Low-power micrograph of a skin biopsy section"></div>
    <div class="abs specimen-frame"></div>

    <div class="abs call-box">
      <div class="call-line">Call Us Now : 800.555.0172</div>
      <div class="address">
        <svg width="20" height="13" viewBox="0 0 20 13" aria-hidden="true"><rect x="0.5" y="0.5" width="19" height="12" fill="#fff" stroke="#fff"/><path d="M1 1 L10 8 L19 1" fill="none" stroke="#e8261c" stroke-width="1.5"/></svg>
        <span>4120 W. Harbor Ave. #310, Seabrook, CA 90000</span>
      </div>
    </div>
    <div class="abs bottom-rule"></div>

    <div class="abs logistics">
      <p>Usually 2-3 day turnaround time depending on the circumstance of the case.</p>
      <p>Courier pick up can usually be arranged.</p>
    </div>
  </main>
</body>
</html>
```